First and Only Single Serving Dental Tooth Powder Company NEEDS Packaging DESIGN

We need a packaging design for a new company based in Florida called 'ZunoDab'. We created the first and only single serving dental tooth powder, for use with or without water. This solves a world problem in numerous faucets. Our product is great for Travelers, Adventure Seekers, Military Personnel, Daily Commuters and any one else wanting the cleanest mouth and freshest breath.

- This is a front and back of a 4(four) by 6(six) package design needed

Target Market(s)

Travelers,Outdoorsman, Adventure seekers, Daily Commuters, and Military Personnel.

Industry/Entity Type

Dental

Requirements
Must have
• -This must fit a package with the dimensions of 4" x 6"
• -four inches by six inches.
• -Earthy/Naturalistic Appeal
• - This is a front and back of a 4(four) by 6(six) package design needed
• -The package will be a White Nylon/Mylar bag
Nice to have
• -Clean your teeth anywhere, anytime...
• -Simple, Convenient, Effective
• -ZunoDab activates without water
• -Proudly made in the USA.
• -Package contains 15 ZunoDab's.
• -The Flavor for the ZunoDab is "Velmo Plum"
• -ZunoDab is for the everyday person on-the-go.
• -Our Story..
• Zunodab was brought to life for moments when time is vital and packing light is a must. We were tired of the same old ordinary way of cleaning our teeth while outdoors, on our adventures, or traveling the globe. The old way required water for it's use which isn't always readily available. With ZunoDab, water is not necessary. The package you hold in your hand contains no ordinary product. In fact, the way you use it is extremely unique and simple.
• Directions: Rip, Pour, Swish, Dispense. Enjoy your adventure responsibly!
Should not have
• A bunch of clutter besides that I am open to ideas.

```html
<!DOCTYPE html>
<html lang="en">
<head>
<meta charset="utf-8">
<title>ZunoDab Dental Tooth Powder – Pouch Front</title>
<link href="https://fonts.googleapis.com/css2?family=Roboto+Condensed:wght@300;400&display=swap" rel="stylesheet">
<style>
  :root {
    --bg: #ffffff;
    --pouch-white: #eeeeec;
    --pouch-white-light: #fafaf9;
    --seam: #d8d8d5;
    --brand-mint: #6dbf94;
    --leaf-green: #4f8a2c;
    --leaf-dark: #345c22;
    --leaf-light: #8cbf4f;
    --copper-dark: #8a4f2c;
    --copper: #c58a62;
    --copper-light: #e6c49c;
    --ink-light: #f4f4f0;
    --badge: #d9c7a8;
  }
  * { margin: 0; padding: 0; box-sizing: border-box; }
  html, body { width: 1200px; height: 1081px; overflow: hidden; background: var(--bg); }
  body { font-family: "Roboto Condensed", "Arial Narrow", sans-serif; }

  .canvas { position: relative; width: 1200px; height: 1081px; background: var(--bg); }

  .pouch {
    position: absolute; left: 390px; top: 140px;
    width: 430px; height: 820px;
    background: var(--leaf-green);
    overflow: hidden;
  }

  .pouch__top {
    position: absolute; left: 0; top: 0; width: 100%; height: 300px;
    background: linear-gradient(180deg, var(--pouch-white-light) 0%, var(--pouch-white) 100%);
  }
  .zip-seam { position: absolute; left: 0; width: 100%; height: 2px; background: var(--seam); }
  .zip-seam--upper { top: 110px; }
  .zip-seam--lower { top: 120px; }

  .brand {
    position: absolute; left: 0; top: 150px; width: 100%;
    display: flex; flex-direction: column; align-items: center; gap: 8px;
  }
  .brand__dot { width: 50px; height: 50px; border-radius: 50%; background: var(--brand-mint); }
  .brand__name { color: var(--brand-mint); font-size: 42px; font-weight: 400; letter-spacing: 1px; line-height: 1; }

  .tagline {
    position: absolute; left: 0; top: 300px; width: 100%; height: 34px;
    background: var(--leaf-green);
    color: var(--ink-light); font-size: 21px; font-style: italic;
    text-align: center; line-height: 34px;
  }

  .title-band {
    position: absolute; left: 0; top: 334px; width: 100%; height: 132px;
    background: linear-gradient(90deg, var(--copper-dark) 0%, var(--copper) 55%, var(--copper-light) 100%);
    display: flex; flex-direction: column; justify-content: center; align-items: center;
  }
  .title-band__text {
    color: var(--ink-light); font-weight: 300; font-size: 48px; line-height: 50px;
    text-align: center; letter-spacing: -1px;
  }

  .pouch__lower {
    position: absolute; left: 0; top: 466px; width: 100%; height: 354px;
    background:
      radial-gradient(ellipse 70% 90% at 70% 55%, var(--leaf-light) 0%, var(--leaf-green) 55%, transparent 75%),
      linear-gradient(180deg, var(--leaf-green) 0%, var(--leaf-dark) 100%);
  }

  .copy { position: absolute; left: 0; width: 100%; text-align: center; color: var(--ink-light); }
  .copy--water { top: 482px; font-size: 24px; }
  .copy--activates { top: 600px; font-size: 23px; font-style: italic; }
  .copy--everyday { top: 640px; font-size: 24px; font-style: italic; line-height: 27px; }

  .flavor {
    position: absolute; left: 0; top: 712px; width: 100%;
    display: flex; justify-content: center; align-items: center; gap: 8px;
    color: var(--ink-light); font-size: 16px; font-style: italic;
  }
  .flavor__icon { width: 22px; height: 22px; }

  .copy--count { top: 748px; font-size: 18px; font-style: italic; }

  .made-badge {
    position: absolute; right: 6px; top: 706px;
    width: 32px; height: 52px; border-radius: 50%;
    background: var(--badge);
  }
</style>
</head>
<body>
  <main class="canvas">
    <section class="pouch" aria-label="ZunoDab tooth powder pouch front">
      <div class="pouch__top">
        <span class="zip-seam zip-seam--upper"></span>
        <span class="zip-seam zip-seam--lower"></span>
        <div class="brand">
          <span class="brand__dot"></span>
          <span class="brand__name">ZunoDab</span>
        </div>
      </div>

      <p class="tagline">Simple, Convenient, Effective</p>

      <div class="title-band">
        <h1 class="title-band__text">DENTAL TOOTH<br>POWDER</h1>
      </div>

      <div class="pouch__lower"></div>

      <p class="copy copy--water">For use with or without water</p>
      <p class="copy copy--activates">activates without water</p>
      <p class="copy copy--everyday">for the everyday<br>person on-the-go</p>

      <div class="flavor">
        <svg class="flavor__icon" viewBox="0 0 22 22" aria-hidden="true">
          <g fill="none" stroke="#f4f4f0" stroke-width="1.4">
            <circle cx="7" cy="7" r="4"/><circle cx="15" cy="7" r="4"/>
            <circle cx="7" cy="15" r="4"/><circle cx="15" cy="15" r="4"/>
          </g>
        </svg>
        <span>Velmo Plum Flavor</span>
      </div>

      <p class="copy copy--count">Package includes 30 stick Paks.</p>

      <span class="made-badge" aria-hidden="true"></span>
    </section>
  </main>
</body>
</html>
```